Business Card and Letterhead for Vantage Psychology

We need a business card design and letterhead to use for our Psychology firm that specializes in psychoeducational assessments and individual therapy. Our motto is Purpose-Driven Assessments, Meaning-Centered Therapy.Our contact information is as follows:
Vantage Psychology
The Marwick Block - 6127-48St.
Box 2716 Olds, AB
T2K 3M8
t 403.555.0148 (VANT)
f 403.555.0172
www.vantagepsychology-example.ca
The business card will be used for two different psychologists so I can supply names nearer to completion. We prefer clean, uncluttered looks.

Target Market(s)

Clients, Educators

Font styles to use
Sans Serif

Colors

Designer to choose colors to be used in the design.

Requirements
Must have
• All relevant contact info, logo, some "white" space.
Nice to have
• It would be nice to see letterhead options that have the logo on the top of the page but also options that have it on the side. I think top of the page is probably our preference.
Should not have
• Too much clutter!

```html
<!DOCTYPE html>
<html lang="en">
<head>
<meta charset="utf-8">
<title>Vantage Psychology – Stationery</title>
<link rel="stylesheet" href="https://fonts.googleapis.com/css2?family=Roboto+Condensed:wght@400;700&family=Roboto:wght@400;500&display=swap">
<style>
  :root {
    --blue: #5bbcd9;
    --orange: #f0a04b;
    --ink: #555a5e;
    --rule: #7a7f83;
    --paper: #ffffff;
    --backdrop: #1f1f1f;
    --watermark: #f1f8fb;
  }
  * { margin: 0; padding: 0; box-sizing: border-box; }
  html, body { width: 1189px; height: 1200px; overflow: hidden; }
  body { background: var(--backdrop); position: relative; font-family: "Roboto", sans-serif; color: var(--ink); }

  .sheet { position: absolute; background: var(--paper); overflow: hidden; }

  /* Letterhead */
  .letterhead { left: 273px; top: 53px; width: 648px; height: 840px; }
  .letterhead .brand { position: absolute; left: 52px; top: 40px; width: 210px; text-align: center; }
  .brand-dot { display: block; margin: 0 auto 10px; border-radius: 50%; background: var(--blue); }
  .letterhead .brand-dot { width: 66px; height: 66px; }
  .brand-name { font-family: "Roboto", sans-serif; font-weight: 500; color: var(--blue); letter-spacing: 0.5px; white-space: nowrap; }
  .letterhead .brand-name { font-size: 17px; }

  .contact { position: absolute; left: 433px; top: 60px; border-left: 1px solid var(--orange); padding-left: 17px; font-size: 10.5px; line-height: 12.5px; }
  .contact .phones { margin-top: 8px; }
  .contact-line { display: flex; align-items: center; gap: 5px; }
  .icon { width: 9px; height: 9px; flex: none; }

  .watermark { position: absolute; left: 325px; top: 560px; width: 318px; height: 318px; border-radius: 50%; background: var(--watermark); }

  .footer-rule { position: absolute; left: 0; right: 0; height: 1px; background: var(--rule); }
  .footer-url { position: absolute; background: var(--paper); font-family: "Roboto Condensed", sans-serif; white-space: nowrap; }
  .footer-url .accent { color: var(--blue); font-weight: 700; }
  .footer-url .accent-2 { color: var(--orange); font-weight: 700; }
  .footer-band { position: absolute; left: 0; right: 0; background: var(--blue); }

  .letterhead .footer-rule { top: 805px; }
  .letterhead .footer-url { right: 60px; top: 797px; padding: 0 6px; font-size: 11px; }
  .letterhead .footer-band { top: 813px; height: 12px; }

  /* Business cards */
  .card { top: 938px; width: 319px; height: 182px; }
  .card-front { left: 273px; background: linear-gradient(180deg, #62bcd6 0%, #b8b890 50%, #efac50 100%); }
  .card-front .brand { position: absolute; left: 0; right: 0; top: 52px; text-align: center; }
  .card-front .brand-dot { width: 52px; height: 52px; background: var(--paper); }
  .card-front .brand-name { color: var(--paper); font-size: 15px; }

  .card-back { left: 602px; }
  .person { position: absolute; left: 19px; top: 26px; }
  .person-name { font-family: "Roboto Condensed", sans-serif; font-weight: 700; font-size: 10px; color: var(--blue); }
  .person-name .credentials { color: var(--orange); }
  .person-role { font-size: 7.5px; margin-top: 2px; }
  .card-back .contact { left: 19px; top: 68px; border: 0; padding: 0; font-size: 7.5px; line-height: 11.5px; }
  .card-back .contact .phones { margin-top: 5px; }
  .card-back .icon { width: 7px; height: 7px; }
  .card-back .brand { position: absolute; left: 172px; top: 85px; width: 130px; text-align: center; }
  .card-back .brand-dot { width: 36px; height: 36px; margin-bottom: 6px; }
  .card-back .brand-name { font-size: 9.5px; }
  .card-back .footer-rule { top: 160px; }
  .card-back .footer-url { right: 8px; top: 154px; padding: 0 4px; font-size: 7px; }
  .card-back .footer-band { top: 166px; height: 7px; }
</style>
</head>
<body>

<section class="sheet letterhead" aria-label="Letterhead">
  <div class="watermark" aria-hidden="true"></div>
  <div class="brand">
    <span class="brand-dot" aria-hidden="true"></span>
    <span class="brand-name">VANTAGE PSYCHOLOGY</span>
  </div>
  <address class="contact" style="font-style:normal">
    <div>The Marwick Block - 6127-48St.</div>
    <div>Box 2716 Olds, AB</div>
    <div>T2K 3M8</div>
    <div class="phones">
      <div class="contact-line"><svg class="icon" viewBox="0 0 10 10"><circle cx="5" cy="5" r="5" fill="#5bbcd9"/><rect x="2.5" y="4" width="5" height="3" rx="0.8" fill="#fff"/></svg>403.555.0148 (VANT)</div>
      <div class="contact-line"><svg class="icon" viewBox="0 0 10 10"><circle cx="5" cy="5" r="5" fill="#5bbcd9"/><rect x="3" y="3" width="4" height="4.5" rx="0.5" fill="#fff"/></svg>403.555.0172</div>
    </div>
  </address>
  <div class="footer-rule"></div>
  <div class="footer-url">www.<span class="accent">VANTAGE</span><span class="accent-2">PSYCHOLOGY</span>-example.ca</div>
  <div class="footer-band"></div>
</section>

<section class="sheet card card-front" aria-label="Business card front">
  <div class="brand">
    <span class="brand-dot" aria-hidden="true"></span>
    <span class="brand-name">VANTAGE PSYCHOLOGY</span>
  </div>
</section>

<section class="sheet card card-back" aria-label="Business card back">
  <div class="person">
    <div class="person-name">DANA WHITCOMBE-HALE, <span class="credentials">M.Ed., RPsych.</span></div>
    <div class="person-role">Registered Psychologist</div>
  </div>
  <address class="contact" style="font-style:normal">
    <div>The Marwick Block - 6127-48St.</div>
    <div>Box 2716 Olds, AB</div>
    <div>T2K 3M8</div>
    <div class="phones">
      <div class="contact-line"><svg class="icon" viewBox="0 0 10 10"><circle cx="5" cy="5" r="5" fill="#5bbcd9"/><rect x="2.5" y="4" width="5" height="3" rx="0.8" fill="#fff"/></svg>403.555.0148 (VANT)</div>
      <div class="contact-line"><svg class="icon" viewBox="0 0 10 10"><circle cx="5" cy="5" r="5" fill="#5bbcd9"/><rect x="3" y="3" width="4" height="4.5" rx="0.5" fill="#fff"/></svg>403.555.0172</div>
      <div class="contact-line"><svg class="icon" viewBox="0 0 10 10"><circle cx="5" cy="5" r="5" fill="#5bbcd9"/><rect x="2.5" y="3.3" width="5" height="3.4" fill="#fff"/></svg>dana@vantagepsychology-example.ca</div>
    </div>
  </address>
  <div class="brand">
    <span class="brand-dot" aria-hidden="true"></span>
    <span class="brand-name">VANTAGE PSYCHOLOGY</span>
  </div>
  <div class="footer-rule"></div>
  <div class="footer-url">www.<span class="accent">VANTAGE</span><span class="accent-2">PSYCHOLOGY</span>-example.ca</div>
  <div class="footer-band"></div>
</section>

</body>
</html>
```